My new Bible based podcast needs a Podcast Cover Design for Vexora directory

I need a Podcast Cover Design design for my podcast listing in Vexora. The podcast is called Morning Lanterns Over Hills. I would like something cheerful, warm, and fresh because I take a non-traditional approach to explaining how the Bible is relevant to people today. My goal is to get back to the original spirituality of the Bible without all the centuries of added man-made doctrines. It would be great to show a sense of peace and hope, with new possibilities. This is not like a floating corporate logo. I need it to be square and full color/design all the way to the edges.

I have resubmitted this project because I did not understand how to ask for a podcast cover design. If you already submitted for me, I apologize for not knowing how the system works. I did not give the best picture of what I needed.

Target Market(s)

People who want a fresh look at the Bible

Industry/Entity Type

Religious

Logo Text

Morning Lanterns Over Hills

Colors

Designer to choose colors to be used in the design.

Requirements
Must have
• It must be square. The design should fill the space. See screen shot below of podcast cover designs on the Christianity/Spirituality page of Vexora directory so you can see where the podcast cover design needs to fit in and stand out.
• The final design will need to be:
• 3,000 x 3,000 pixels (but readable at 150 x 150)
• 72 dpi
• .jpg or .png format
• rgb color space
Nice to have
• Perhaps an open book suggesting the Bible, but not necessary.
Should not have
• No microphones or airwaves.

```html
<!DOCTYPE html>
<html lang="en">
<head>
<meta charset="utf-8">
<title>Morning Lanterns Over Hills — Podcast Cover</title>
<link rel="stylesheet" href="https://fonts.googleapis.com/css2?family=Oswald:wght@200;600&display=swap">
<style>
  :root {
    --cover-blue: #2c5ba8;
    --title-white: #f4f2fb;
    --title-yellow: #fdca05;
    --photo-top: #b9b9bd;
    --photo-book: #1f1c1f;
    --photo-denim: #3b4a66;
  }
  html, body {
    margin: 0;
    padding: 0;
    width: 1200px;
    height: 1200px;
    overflow: hidden;
    background: var(--cover-blue);
  }
  .cover {
    position: relative;
    width: 1200px;
    height: 1200px;
    background: var(--cover-blue);
    overflow: hidden;
    font-family: "Oswald", "Arial Narrow", sans-serif;
  }
  .cover__photo {
    position: absolute;
    left: 0;
    top: 0;
    width: 470px;
    height: 1200px;
    background: linear-gradient(
      180deg,
      var(--photo-top) 0%,
      var(--photo-book) 12%,
      var(--photo-book) 58%,
      var(--photo-denim) 78%,
      var(--photo-denim) 100%
    );
  }
  .cover__rule {
    position: absolute;
    height: 21px;
  }
  .cover__rule--top {
    left: 786px;
    width: 380px;
    top: 94px;
    background: var(--title-yellow);
  }
  .cover__rule--bottom {
    left: 532px;
    width: 638px;
    top: 1082px;
    background: var(--title-white);
  }
  .cover__title {
    position: absolute;
    right: 34px;
    top: 156px;
    width: 660px;
    margin: 0;
    display: grid;
    grid-template-rows: repeat(4, 200px);
    row-gap: 27px;
    justify-items: end;
    align-items: center;
    text-transform: uppercase;
    white-space: nowrap;
  }
  .cover__line {
    display: block;
    line-height: 1;
  }
  .cover__line--light { font-weight: 200; }
  .cover__line--bold { font-weight: 600; }
  .cover__line--white { color: var(--title-white); }
  .cover__line--yellow { color: var(--title-yellow); }
  .cover__line--morning { font-size: 196px; }
  .cover__line--lanterns { font-size: 160px; }
  .cover__line--over { font-size: 248px; }
  .cover__line--hills { font-size: 248px; }
</style>
</head>
<body>
  <main class="cover">
    <div class="cover__photo" role="img" aria-label="Photo of a person in a grey top and jeans holding a black Bible at their side"></div>

    <div class="cover__rule cover__rule--top"></div>

    <h1 class="cover__title">
      <span class="cover__line cover__line--light cover__line--white cover__line--morning">Morning</span>
      <span class="cover__line cover__line--bold cover__line--white cover__line--lanterns">Lanterns</span>
      <span class="cover__line cover__line--bold cover__line--yellow cover__line--over">Over</span>
      <span class="cover__line cover__line--light cover__line--yellow cover__line--hills">Hills</span>
    </h1>

    <div class="cover__rule cover__rule--bottom"></div>
  </main>
</body>
</html>
```